Gentle Harbor Label

We need labels for a new brewery called "Gentle Harbor":

We need one label, that we can slightly change to suit the style of liquid. So far the beers are:
- XPA
- Pale ALe
- IPA
- Black Ale

We want creative, fun labels, nothing traditional. but appropriate to suit all international markets.

Design was promoted in LOGO & not in Design, so we got a lot of logo's but very little designs for bottles/cans.

Gentle Harbor Brewing

```html
<!DOCTYPE html>
<html lang="en">
<head>
<meta charset="utf-8">
<title>Gentle Harbor Pale Ale Label</title>
<link rel="stylesheet" href="https://fonts.googleapis.com/css2?family=Alfa+Slab+One&family=Libre+Baskerville:wght@700&family=Playfair+Display+SC:wght@700&family=Architects+Daughter&family=Courier+Prime&display=swap">
<style>
  :root {
    --page: #e9e7e3;
    --label-black: #1a1012;
    --splash-red: #a81f2c;
    --wall-teal: #3fb6c8;
    --wall-deep: #1f7d8c;
    --creature-red: #8e1b28;
    --creature-dark: #5a1018;
    --style-green: #5da54a;
    --ink-light: #f2f2ee;
    --ink-dark: #111111;
  }
  * { margin: 0; padding: 0; box-sizing: border-box; }
  html, body {
    width: 1200px;
    height: 733px;
    overflow: hidden;
    background: var(--page);
  }
  .canvas {
    position: relative;
    width: 1200px;
    height: 733px;
  }
  .label {
    position: absolute;
    left: 390px;
    top: 36px;
    width: 420px;
    height: 660px;
    overflow: hidden;
    background: var(--wall-teal);
    box-shadow: 0 6px 24px rgba(0,0,0,0.18);
  }
  .label__head {
    position: absolute;
    left: 0; top: 0;
    width: 420px; height: 215px;
    background: linear-gradient(100deg, var(--label-black) 0%, var(--label-black) 62%, var(--splash-red) 100%);
  }
  .label__tagline {
    position: absolute;
    left: 28px; top: 42px;
    font-family: "Playfair Display SC", serif;
    font-weight: 700;
    font-size: 15px;
    letter-spacing: 0.3px;
    color: var(--ink-light);
  }
  .label__brand {
    position: absolute;
    left: 28px; top: 136px;
    font-family: "Alfa Slab One", serif;
    font-weight: 400;
    font-size: 36px;
    line-height: 36px;
    color: var(--ink-light);
    letter-spacing: 0.5px;
  }
  .label__wall {
    position: absolute;
    left: 0; top: 215px;
    width: 420px; height: 445px;
    background: linear-gradient(180deg, var(--wall-teal) 0%, #36a7ba 60%, var(--wall-deep) 100%);
  }
  .label__creature {
    position: absolute;
    left: 340px; top: 150px;
    width: 80px; height: 420px;
    background: linear-gradient(180deg, var(--creature-red) 0%, var(--creature-dark) 100%);
  }
  .label__specs {
    position: absolute;
    left: 30px; top: 252px;
    width: 250px;
    display: flex;
    justify-content: space-between;
    font-family: "Courier Prime", monospace;
    font-size: 13px;
    color: var(--ink-light);
  }
  .label__style {
    position: absolute;
    left: 30px; top: 276px;
    width: 236px; height: 66px;
    background: var(--style-green);
    display: flex;
    align-items: center;
    padding-left: 2px;
    font-family: "Libre Baskerville", serif;
    font-weight: 700;
    font-size: 38px;
    color: var(--ink-dark);
    white-space: nowrap;
  }
  .label__story {
    position: absolute;
    left: 32px; top: 362px;
    width: 300px;
    font-family: "Architects Daughter", cursive;
    font-size: 15px;
    line-height: 34px;
    text-transform: uppercase;
    color: var(--ink-light);
    white-space: nowrap;
  }
  .label__story span { display: block; }
</style>
</head>
<body>
<main class="canvas">
  <section class="label">
    <div class="label__head" role="img" aria-label="Red paint splash texture over black"></div>
    <p class="label__tagline">Dangerously Different Craft Beer</p>
    <h1 class="label__brand">GENTLE<br>HARBOR</h1>
    <div class="label__wall" role="img" aria-label="Painted teal brick wall pattern"></div>
    <div class="label__creature" role="img" aria-label="Illustration of a red furry character peeking in from the edge"></div>
    <div class="label__specs"><span>375ML</span><span>4.2% ABV</span></div>
    <h2 class="label__style">Pale Ale</h2>
    <p class="label__story">
      <span>We started Gentle Harbor</span>
      <span>brewing for utility &amp; curiosity.</span>
      <span>Our passion for local, fresh</span>
      <span>craft beer grew. Any craft</span>
      <span>brewer worth anything started</span>
      <span>somewhere as a home brewer.</span>
      <span>We learned the craft and we</span>
      <span>invested our all.</span>
    </p>
  </section>
</main>
</body>
</html>
```